GownLoom.com will be an online bespoke garment creator, specifically around designing your own Wedding Dress. It will enable you to specify your own material, colours and patterns and customized features such as bows, sequins, diamantes, and more from a selection of per-defined base garments and customize them to your taste.
The concept is similar to:
www.threadwellstudio.com
But the design should reflect more like
www.velmarrow.com
www.pindle.com - (in particular the build elements)
www.korvo.com
It will be aimed at the Female marketplace. However this does not mean to use pink or portray the brand in very girly way. It should use good white space, and look very classy. not too busy, but functional and elegant, with a focus on stable and responsible site that will deliver. A wedding dress is an important purchase and to trust a company to make one for you from a distance takes a lot of trust from the customer perspective.
We want to first create the homepage and "build the dress" pages, which will consist of Enter your Measurements, Choose a Base Silhouette Style, Choose Fabric, Choose Colors, Customize Dress, Summary, Order Page, Thank you Page.
It will then have generic About us, How to Measure, Agent Locator, How it works, Contact, Order Samples, Support.
A very basic wire frame was created here to aid development, but the branding is being developed, so do not use any of it for inspiration just a visual interpretation - http://pageyard4.info/bespoke/
The link above is merely an idea on what areas the site will have. The actual design and colour scheme should reflect these sites.
The branding is also here - www.gownloom.com not the one used within that link.
The site will enable you to log in, save your designs and your delivery and measurement information. It will also offer the usual social media buttons to share the design and ability to leave comments.
This will be the first draft and the winning design will get to design the other pages and future work associated to the site.
thanks!

```html
<!DOCTYPE html>
<html lang="en">
<head>
<meta charset="utf-8">
<title>GownLoom – Bespoke Wedding Dresses</title>
<link href="https://fonts.googleapis.com/css2?family=Arimo:wght@400;700&family=Noto+Serif:wght@400;700&family=Great+Vibes&family=Oswald:wght@300;400&display=swap" rel="stylesheet">
<style>
:root{
  --ink:#1a1a1a;
  --text:#333;
  --muted:#666;
  --soft:#999;
  --line:#d8d8d8;
  --hero:#454545;
  --band-top:#d2d2d2;
  --band-bottom:#ffffff;
  --btn-top:#6a6a6a;
  --btn-bottom:#2b2b2b;
  --white:#fff;
}
*{margin:0;padding:0;box-sizing:border-box}
html,body{width:960px;height:1200px;overflow:hidden;background:var(--white)}
body{position:relative;font-family:"Arimo",Arial,sans-serif;color:var(--text)}
.abs{position:absolute}
a{color:inherit;text-decoration:none}

.utility{right:174px;top:18px;font-size:8px;color:var(--text)}
.utility span{margin:0 4px;color:var(--muted)}
.logo{left:174px;top:36px;font-family:"Arimo",Arial,sans-serif;font-weight:700;font-size:22px;letter-spacing:2px;color:#3a3a3a}
.search{left:596px;top:48px;width:190px;height:19px;border:1px solid #aaa;border-radius:10px;font-size:7px;color:var(--soft);padding:5px 8px}
.search-btn{right:0;top:-1px;width:24px;height:19px;border-radius:0 10px 10px 0;background:linear-gradient(var(--btn-top),var(--btn-bottom))}

.main-nav{left:174px;top:103px;width:612px;display:flex;justify-content:space-between;font-family:"Noto Serif",Georgia,serif;font-size:9px;color:var(--ink);padding:0 18px}
.main-nav b{font-weight:700;font-size:10px}
.rule{left:83px;width:793px;height:3px;background:var(--ink)}

.hero{left:173px;top:121px;width:613px;height:249px;background:var(--hero);overflow:hidden}
.hero-photo{top:0;height:249px}
.hero-title{left:196px;top:20px;font-family:"Great Vibes",cursive;color:var(--white);font-size:58px;white-space:nowrap}
.hero-title small{font-size:22px}
.hero-copy{left:204px;top:103px;font-family:"Oswald",sans-serif;font-weight:300;color:var(--white);font-size:11px;line-height:14px}
.hero-btn{left:202px;top:146px;width:88px;height:24px;border-radius:6px;border:1px solid #888;background:linear-gradient(#6b6b6b,#333);color:var(--white);font-family:"Oswald",sans-serif;font-weight:300;font-size:11px;text-align:center;line-height:22px}
.arrow{top:95px;color:#777;font-size:30px;font-family:"Arimo",sans-serif}

.band{left:83px;top:370px;width:793px;height:80px;background:linear-gradient(var(--band-top),var(--band-bottom))}
.panel{top:370px;width:203px;height:79px;background:linear-gradient(#f2f2f2,#d7d7d7);border-right:1px solid #fff;padding:8px 10px}
.panel h3{font-size:11px;font-weight:700;color:#333;margin-bottom:3px}
.panel p{font-size:7.5px;line-height:10px;color:var(--muted);width:120px}
.btn{display:inline-block;position:absolute;height:17px;padding:0 8px;border-radius:3px;background:linear-gradient(var(--btn-top),var(--btn-bottom));color:var(--white);font-size:8px;line-height:17px;text-align:center}
.panel .btn{bottom:6px;left:50%;transform:translateX(-50%);white-space:nowrap}
.panel-art{position:absolute;right:10px;top:10px;width:44px;height:44px}

h2.section{font-weight:400;font-size:16px;color:var(--ink)}
.para{font-size:6.8px;line-height:9px;color:var(--muted)}
.photo{box-shadow:0 2px 3px rgba(0,0,0,.35);border:1px solid #ccc}
.sep{height:10px;background:radial-gradient(ellipse at top,rgba(0,0,0,.12),rgba(0,0,0,0) 70%)}
.divider{left:578px;top:462px;width:1px;height:506px;background:var(--line)}

.post{width:200px;height:44px}
.post .thumb{position:absolute;left:0;top:0;width:42px;height:42px;background:linear-gradient(#6b6152,#2f2a24)}
.post h4{position:absolute;left:48px;top:0;font-size:8.5px;font-weight:400;color:#333;line-height:11px}
.post p{position:absolute;left:48px;font-size:6.3px;line-height:8px;color:var(--muted)}

.quote{width:200px}
.quote .avatar{position:absolute;left:4px;top:0;width:38px;height:38px;border-radius:50%;background:radial-gradient(#ddd,#888);border:2px solid #ccc}
.quote p{position:absolute;left:48px;top:0;font-size:6.5px;line-height:9px;font-weight:700;font-style:italic;color:#444;width:150px}
.quote .by{position:absolute;left:48px;top:34px;font-size:6.5px;color:#222}
.quote .by span{color:var(--muted);margin-left:3px;font-size:5.5px}

.video{left:586px;top:486px;width:200px;height:169px;background:#0b0b0b}
.pop{left:588px;width:198px;height:36px;border-bottom:1px solid var(--line)}
.pop .thumb{position:absolute;left:1px;top:0;width:55px;height:33px;border:1px solid #aaa;background:linear-gradient(#e8e8e8,#8a8a8a)}
.pop p{position:absolute;left:61px;top:8px;font-size:8px;line-height:10px;color:#333}
.email{left:586px;top:908px;width:195px;height:19px;border:1px solid #aaa;font-size:7.5px;color:var(--soft);padding:4px 5px}

.foot-col h5{font-size:10px;font-weight:400;color:var(--ink);margin-bottom:8px}
.foot-col li{list-style:none;font-size:8px;color:var(--muted);line-height:15px}
.foot-col li::before{content:"";display:inline-block;width:5px;height:5px;border:1px solid #888;margin-right:4px;vertical-align:0}
.social{top:1021px;width:15px;height:15px;border-radius:3px;background:#7b8ea8}
.foot-logo{left:612px;top:1052px;font-weight:700;font-size:20px;letter-spacing:2px;color:#3a3a3a}
.card{top:1144px;width:17px;height:11px;border-radius:2px}
.copyright{left:0;width:960px;top:1167px;text-align:center;font-size:7px;color:#222}
</style>
</head>
<body>

<div class="abs utility">My Account<span>|</span>Manage Order<span>|</span>Order Status<span>|</span>Log In<span>|</span>Register</div>
<div class="abs logo">GOWNLOOM</div>
<div class="abs search">Search:<div class="abs search-btn"></div></div>

<nav class="abs main-nav"><a>HOME</a><a>ABOUT US</a><a>AGENT LOCATOR</a><a>MEASURE YOURSELF</a><a>CONTACT US</a><b>Refer a Friend</b></nav>
<div class="abs rule" style="top:118px"></div>

<section class="abs hero">
  <div class="abs hero-photo" role="img" aria-label="Photo of a bride in a white veil and gown holding a bouquet" style="left:20px;width:150px;background:linear-gradient(90deg,#5a5a5a,#d9d9d9 40%,#bfbfbf 70%,#545454)"></div>
  <div class="abs hero-photo" role="img" aria-label="Photo of a smiling bride in an off-shoulder white gown" style="left:448px;width:165px;background:linear-gradient(90deg,#4a4a4a,#9a9a9a 30%,#e0e0e0 75%,#cfcfcf)"></div>
  <div class="abs arrow" style="left:8px">‹</div>
  <div class="abs arrow" style="right:10px">›</div>
  <div class="abs hero-title">Choose <small>Color, Fabric &amp; Style</small></div>
  <div class="abs hero-copy">Create &amp; Order your own online Bespoke dress,<br>with just few easy steps</div>
  <div class="abs hero-btn">Get Started!</div>
</section>

<div class="abs band"></div>
<div class="abs panel" style="left:173px">
  <h3>Choose Fabric &amp; Color</h3>
  <p>Choose fabric and color to fit dress by selecting Choose fabric &amp; color button</p>
  <div class="panel-art" role="img" aria-label="Patterned fabric swatch" style="background:linear-gradient(#fafafa,#cfcfcf)"></div>
  <a class="btn">Choose Fabric &amp; Color</a>
</div>
<div class="abs panel" style="left:377px">
  <h3>Measure Yourself</h3>
  <p>Measure your made to fit design Gown by selecting Measure now button</p>
  <div class="panel-art" role="img" aria-label="Coiled measuring tape" style="background:radial-gradient(#eee,#aaa 60%,transparent 70%)"></div>
  <a class="btn">Measure Now</a>
</div>
<div class="abs panel" style="left:581px;border-right:0;border-radius:0 0 6px 0">
  <h3>Agent Locator</h3>
  <p>Find Agent in your area and book appointment by selecting Find agent button.</p>
  <svg class="panel-art" viewBox="0 0 44 44" aria-hidden="true"><path d="M22 40 L12 24 A12 12 0 1 1 32 24 Z" fill="none" stroke="#555" stroke-width="4"/><circle cx="22" cy="17" r="4" fill="#555"/></svg>
  <a class="btn">Find Agent</a>
</div>

<h2 class="abs section" style="left:173px;top:467px">Wedding Dress at GownLoom</h2>
<div class="abs photo" role="img" aria-label="Photo of white wedding dresses hanging on a rail" style="left:174px;top:493px;width:92px;height:70px;background:linear-gradient(#b7a985,#eee 55%,#cfd6dc)"></div>
<p class="abs para" style="left:272px;top:494px;width:300px">Lorem ipsum dolor sit amet, consectetur adipiscing elit. Sed mattis nulla in urna dapibus pulvinar. Donec sit amet enim enim, quis convallis tellus. Nulla risus odio, blandit ac suscipit vel, rhoncus eu libero. Nullam ligula massa, cursus sed ultrices sed, accumsan nec ante. Suspendisse congue malesuada ante eu fringilla. Proin sit amet arcu dui, quis hendrerit dui. Praesent sed iaculis massa. Suspendisse in urna ligula. Aliquam et mi sed justo convallis sagittis non vitae ligula. Quisque neque sapien, viverra vitae molestie eleifend, consectetur nec odio. Suspendisse vel posuere nisl. Cras eget risus est.</p>
<a class="btn" style="left:513px;top:564px">View more</a>
<div class="abs sep" style="left:190px;top:596px;width:370px"></div>

<h2 class="abs section" style="left:173px;top:616px">Style Advisor | The Blog</h2>
<p class="abs" style="left:173px;top:640px;width:390px;font-size:8px;line-height:10px;color:#333">Want to know what's going on behind the scenes or our style recommendations? Welcome to our blog...</p>

<div class="abs post" style="left:174px;top:666px"><div class="thumb" role="img" aria-label="Portrait photo of a woman"></div><h4>A touch of Australia in a suit...</h4><p style="top:14px">Those of you who flicked over to the local channel last night might have spotted a familiar face - our St ...</p></div>
<div class="abs post" style="left:379px;top:666px"><div class="thumb" role="img" aria-label="Photo of a man in a suit"></div><h4>It's 'Mission Unlikely' to find<br>the suit</h4><p style="top:25px">We've had so many requests for this suit or one like it that I thought it was about time o ...</p></div>
<div class="abs post" style="left:174px;top:719px"><div class="thumb" role="img" aria-label="Photo of a man in a tailored blazer"></div><h4>A gold medal for style...</h4><p style="top:14px">The Summer Games has ended, and what a success it has been. Not just for the home side, but for the games ...</p></div>
<div class="abs post" style="left:379px;top:719px"><div class="thumb" role="img" aria-label="Photo of a groomsman in a suit"></div><h4>The Lucky Lads: Groomsmen<br>Matching Wedding Suit ...</h4><p style="top:25px">he Lucky Lads Somebody once asked 'Whatever happened to the lucky lads?' Well, I can tell you. They ...</p></div>
<div class="abs post" style="left:174px;top:772px"><div class="thumb" role="img" aria-label="Photo of a man in dapper shoes and suit"></div><h4>Bring them back: SPATS!</h4><p style="top:14px">Yes, you heard me, spats are cool! They are dapper and can glam up a drab pair of shoes. You can mak ...</p></div>
<div class="abs post" style="left:379px;top:772px"><div class="thumb" role="img" aria-label="Photo of a man in cowboy style wedding wear"></div><h4>Maren's Wedding Themes: Part<br>3, Giddy up cowboy</h4><p style="top:25px">This isn't one of the most popular themes these days but is definitely one of the most fun.</p></div>
<div class="abs sep" style="left:190px;top:835px;width:370px"></div>

<h2 class="abs section" style="left:173px;top:849px">Testimonials</h2>
<div class="abs quote" style="left:174px;top:878px"><div class="avatar" role="img" aria-label="Client portrait"></div><p>“Lorem ipsum site dolor text here.Lorem ipsum site dolor text.Lorem ipsum site dolor text.Lorem ipsum site dolor text.”</p><div class="by">By: Client Name Here<span>Technical Director</span></div></div>
<div class="abs quote" style="left:379px;top:878px"><div class="avatar" role="img" aria-label="Client portrait"></div><p>“Lorem ipsum site dolor text here.Lorem ipsum site dolor text.Lorem ipsum site dolor text.Lorem ipsum site dolor text.”</p><div class="by">By: Client Name Here<span>Technical Director</span></div></div>
<a class="btn" style="left:510px;top:927px">View more</a>

<div class="abs divider"></div>

<h2 class="abs section" style="left:586px;top:466px">How We Work</h2>
<div class="abs video">
  <div class="abs" role="img" aria-label="Video still of a wedding bodice being measured with a tape" style="left:0;top:0;width:200px;height:150px;background:radial-gradient(ellipse at 50% 70%,#e9e9e9,#9a9a9a 40%,#0b0b0b 65%)"></div>
  <svg class="abs" style="left:72px;top:54px" width="54" height="38" viewBox="0 0 54 38" aria-hidden="true"><rect width="54" height="38" rx="4" fill="#333" opacity=".8"/><path d="M21 10 L36 19 L21 28 Z" fill="#999"/></svg>
  <div class="abs" style="left:0;top:150px;width:200px;height:19px;background:linear-gradient(#ddd,#aaa)"></div>
  <div class="abs" style="left:20px;top:154px;width:160px;height:2px;background:#666"></div>
</div>

<h2 class="abs section" style="left:586px;top:681px">Most Popular</h2>
<div class="abs pop" style="top:706px"><div class="thumb" role="img" aria-label="Photo of a bride and groom"></div><p>Wedding suit for your special day</p></div>
<div class="abs pop" style="top:752px"><div class="thumb" role="img" aria-label="Photo of a man in a tailored suit"></div><p>Bespoke tailored suit in your favourite fabric</p></div>
<div class="abs pop" style="top:799px"><div class="thumb" role="img" aria-label="Photo of a man in an overcoat"></div><p>Tailored overcoats for a distinguished winter look</p></div>
<a class="btn" style="left:724px;top:834px">View more</a>

<h2 class="abs section" style="left:586px;top:871px">Our Newsletter</h2>
<p class="abs" style="left:586px;top:894px;font-size:8px;color:#222">Sign up for our newsletter</p>
<div class="abs email">Enter your email address</div>
<a class="btn" style="left:722px;top:931px;padding:0 10px">Subscribe</a>

<div class="abs rule" style="top:970px"></div>

<div class="abs foot-col" style="left:173px;top:986px"><h5>Navigation</h5><ul><li>Lorem ipsum dolor</li><li>Sit amet, consecte</li><li>Tur adipiscing elit</li><li>Sed mattis nulla in</li><li>Urna dapibus pulv</li><li>Inar Donec sit amet</li><li>Enim enim, quis</li></ul></div>
<div class="abs foot-col" style="left:279px;top:986px"><h5>Company</h5><ul><li>Lorem ipsum dolor</li><li>Sit amet, consecte</li><li>Tur adipiscing elit</li><li>Sed mattis nulla in</li><li>Urna dapibus pulv</li><li>Inar Donec sit amet</li><li>Enim enim, quis</li></ul></div>
<div class="abs foot-col" style="left:388px;top:986px"><h5>Media</h5><ul><li>Lorem ipsum dolor</li><li>Sit amet, consecte</li><li>Tur adipiscing elit</li><li>Sed mattis nulla in</li><li>Urna dapibus pulv</li><li>Inar Donec sit amet</li><li>Enim enim, quis</li></ul></div>
<div class="abs foot-col" style="left:506px;top:986px"><h5>My Account</h5><ul><li>Lorem ipsum dolor</li><li>Sit amet, consecte</li><li>Tur adipiscing elit</li><li>Sed mattis nulla in</li><li>Urna dapibus pulv</li><li>Inar Donec sit amet</li><li>Enim enim, quis</li></ul></div>
<div class="abs" style="left:602px;top:980px;width:1px;height:138px;background:var(--line)"></div>

<div class="abs social" style="left:704px"></div>
<div class="abs social" style="left:725px"></div>
<div class="abs social" style="left:747px"></div>
<div class="abs social" style="left:769px"></div>
<div class="abs foot-logo">GOWNLOOM</div>

<div class="abs sep" style="left:190px;top:1122px;width:580px"></div>

<div class="abs card" style="left:405px;background:#9ab"></div>
<div class="abs card" style="left:425px;background:#cc9"></div>
<div class="abs card" style="left:445px;background:#d99"></div>
<div class="abs card" style="left:471px;background:#a6c"></div>
<div class="abs card" style="left:493px;background:#ddd"></div>
<div class="abs card" style="left:514px;background:#ec4"></div>
<div class="abs card" style="left:536px;background:#eb9"></div>
<p class="abs copyright">Copyright © 2012 GownLoom.com All rights reserved!</p>

</body>
</html>
```